Web Developer Needs a Business Card Design

I need a personal business card design that represents me as a web developer for potential employers. I would like the background to be a dark color on the front for contrast with my logo and name. The back will have all my information along with a smaller version of the logo. I want something with a modern look and feel, not too conservative. This will be used for potential employers and freelance work.

Industry/Entity Type

Business

Contact Information for Business Card

Front should have my logo and name. The back should have all my personal information which would include: name: Tom Brevardi, phone: 570-614-9083, email: tombrevardi@mailwisp.com, website url: www.tombrevardi.com, logo, web developer.

Font styles to use
Sans Serif

Requirements
Must have
• Must include my logo. The color palette base color will be the logo color.

```html
<!DOCTYPE html>
<html lang="en">
<head>
<meta charset="utf-8">
<title>Tom Brevardi — Web Developer Business Card</title>
<link rel="stylesheet" href="https://fonts.googleapis.com/css2?family=Josefin+Sans:wght@400;700&family=Lora:wght@400&display=swap">
<style>
  :root {
    --paper: #dfe7e6;
    --paper-light: #e9efee;
    --paper-shade: #d2dbda;
    --teal: #6cc7b3;
    --ink: #343434;
    --ink-soft: #3a3a3a;
  }
  * { margin: 0; padding: 0; box-sizing: border-box; }
  html, body { width: 1200px; height: 704px; overflow: hidden; }
  body { background: var(--paper); }
  .card {
    position: relative;
    width: 1200px;
    height: 704px;
    background: radial-gradient(ellipse at 40% 35%, var(--paper-light) 0%, var(--paper) 55%, var(--paper-shade) 100%);
    font-family: "Josefin Sans", sans-serif;
    color: var(--ink);
  }
  .brand-mark {
    position: absolute;
    left: 165px;
    top: 158px;
    width: 312px;
    height: 312px;
    border: 13px solid var(--teal);
    border-radius: 50%;
    display: flex;
    align-items: center;
    justify-content: center;
  }
  .brand-name {
    font-family: "Josefin Sans", sans-serif;
    font-weight: 700;
    font-size: 34px;
    color: var(--teal);
    letter-spacing: 0.04em;
    white-space: nowrap;
  }
  .divider {
    position: absolute;
    left: 600px;
    top: 72px;
    width: 5px;
    height: 509px;
    background: var(--teal);
  }
  .role {
    position: absolute;
    left: 767px;
    top: 132px;
    font-weight: 400;
    font-size: 31px;
    letter-spacing: 0.01em;
    color: var(--ink);
    text-transform: uppercase;
    white-space: nowrap;
  }
  .name {
    position: absolute;
    left: 693px;
    top: 196px;
    font-weight: 700;
    font-size: 44px;
    letter-spacing: 0.185em;
    color: var(--ink);
    text-transform: uppercase;
    white-space: nowrap;
  }
  .contact-list { list-style: none; }
  .contact-item {
    position: absolute;
    display: flex;
    align-items: center;
    font-family: "Lora", serif;
    font-size: 27px;
    color: var(--ink-soft);
    white-space: nowrap;
  }
  .contact-item svg { flex: none; }
  .contact-phone { left: 736px; top: 287px; }
  .contact-phone .contact-text { margin-left: 17px; }
  .contact-email { left: 726px; top: 364px; }
  .contact-email .contact-text { margin-left: 16px; }
  .contact-web { left: 718px; top: 439px; }
  .contact-web .contact-text { margin-left: 16px; }
</style>
</head>
<body>
  <main class="card">
    <div class="brand-mark">
      <span class="brand-name">Tom Brevardi</span>
    </div>

    <div class="divider"></div>

    <p class="role">Web Developer</p>
    <h1 class="name">Tom Brevardi</h1>

    <ul class="contact-list">
      <li class="contact-item contact-phone">
        <svg width="54" height="54" viewBox="0 0 54 54" aria-hidden="true">
          <path d="M14 6 l8 11 -5 5 c3 7 8 12 15 15 l5 -5 11 8 -4 8 c-3 3 -8 3 -14 0 C18 43 11 36 7 24 c-3 -6 -3 -11 0 -14 z" fill="var(--ink)"/>
          <path d="M30 12 a12 12 0 0 1 12 12" stroke="var(--ink)" stroke-width="3.5" fill="none" stroke-linecap="round"/>
          <path d="M31 4 a19 19 0 0 1 19 19" stroke="var(--ink)" stroke-width="3.5" fill="none" stroke-linecap="round"/>
        </svg>
        <span class="contact-text">570-614-9083</span>
      </li>
      <li class="contact-item contact-email">
        <svg width="64" height="62" viewBox="0 0 64 62" aria-hidden="true">
          <path d="M3 24 L32 3 L61 24 L32 42 Z" fill="var(--ink)"/>
          <rect x="3" y="24" width="58" height="35" fill="none" stroke="var(--ink)" stroke-width="2.5"/>
          <path d="M3 59 L26 38 M61 59 L38 38 M3 24 L32 44 L61 24" fill="none" stroke="var(--ink)" stroke-width="2.5"/>
          <text x="32" y="28" text-anchor="middle" font-family="Lora, serif" font-size="16" fill="#ffffff">@</text>
        </svg>
        <span class="contact-text">tombrevardi@mailwisp.com</span>
      </li>
      <li class="contact-item contact-web">
        <svg width="72" height="72" viewBox="0 0 74 74" aria-hidden="true">
          <g fill="none" stroke="var(--ink)" stroke-width="4">
            <circle cx="37" cy="37" r="34"/>
            <ellipse cx="37" cy="37" rx="15" ry="34"/>
            <line x1="37" y1="3" x2="37" y2="71"/>
            <line x1="3" y1="37" x2="71" y2="37"/>
            <path d="M9 19 H65 M9 55 H65"/>
          </g>
        </svg>
        <span class="contact-text">www.tombrevardi.com</span>
      </li>
    </ul>
  </main>
</body>
</html>
```